Gemstone Jewelry Online Shop Needs a Banner Design

We need a banner design for a new gemstone Jewelry Online Shop based in the U.S. called "Velanor". One of our selling points is "never fall out of stone". We want to express: a Party Queen doesn't need to worry whenever she may meet an embarrassing moment - a stone of jewelry falls out at a very important occasion. Please insert one of attached images. Please visit our website for more details: http://velanor-shop.example/
The banner size: 1200*628
If you think other images at our website are better, please let us know. Many thanks and looking forward to your beautiful and creative designs!

Industry/Entity Type

Jewelry

```html
<!DOCTYPE html>
<html lang="en">
<head>
<meta charset="utf-8">
<title>Velanor – Fine Gemstone Jewelry Banner</title>
<link rel="stylesheet" href="https://fonts.googleapis.com/css2?family=Gabriela&family=Montserrat:wght@500&display=swap">
<style>
  :root {
    --page-bg: #ffffff;
    --violet-deep: #4f1fa8;
    --violet-mid: #6a35c4;
    --lavender: #8f6fe0;
    --glow-blue: #b9c8f4;
    --ink-dark: #160c2a;
    --text-light: #ffffff;
    --tag-grey: #e8e4f2;
    --brand-ink: #0f2412;
    --product-light: #c9c3e8;
    --product-deep: #8a5fd6;
  }
  * { margin: 0; padding: 0; box-sizing: border-box; }
  html, body {
    width: 1200px;
    height: 691px;
    overflow: hidden;
    background: var(--page-bg);
  }
  .banner {
    position: absolute;
    left: 22px;
    top: 38px;
    width: 1154px;
    height: 603px;
    overflow: hidden;
    background: var(--violet-deep);
    font-family: "Gabriela", serif;
  }
  .banner__backdrop {
    position: absolute;
    inset: 0;
    width: 100%;
    height: 100%;
  }
  .banner__product {
    position: absolute;
    left: 0;
    top: 0;
    width: 538px;
    height: 538px;
    background: linear-gradient(160deg, var(--product-light) 0%, var(--product-deep) 100%);
    opacity: 0.55;
  }
  .slogan {
    position: absolute;
    left: 96px;
    top: 86px;
    color: var(--text-light);
    font-size: 44px;
    line-height: 50px;
    font-weight: 400;
  }
  .slogan__line { display: block; }
  .slogan__line--indent { padding-left: 72px; }
  .brand {
    position: absolute;
    right: 150px;
    top: 88px;
    text-align: right;
  }
  .brand__name {
    display: block;
    color: var(--brand-ink);
    font-size: 90px;
    line-height: 100px;
    font-weight: 400;
  }
  .brand__tagline {
    display: block;
    margin-top: -4px;
    font-family: "Montserrat", sans-serif;
    font-weight: 500;
    font-size: 18px;
    letter-spacing: 0.5px;
    color: var(--tag-grey);
  }
  .pitch {
    position: absolute;
    right: 94px;
    top: 262px;
    width: 620px;
    text-align: right;
    color: var(--ink-dark);
    font-size: 27px;
    line-height: 48px;
  }
  .pitch__line { display: block; }
  .visit {
    position: absolute;
    right: 94px;
    top: 484px;
    color: var(--text-light);
    font-size: 28px;
    line-height: 40px;
  }
</style>
</head>
<body>
  <section class="banner">
    <svg class="banner__backdrop" viewBox="0 0 1154 603" preserveAspectRatio="none" role="img" aria-label="Soft violet floral background">
      <defs>
        <radialGradient id="flower-glow" cx="0.3" cy="0.72" r="0.45">
          <stop offset="0" stop-color="#b9c8f4" stop-opacity="0.85"/>
          <stop offset="0.5" stop-color="#8f6fe0" stop-opacity="0.5"/>
          <stop offset="1" stop-color="#4f1fa8" stop-opacity="0"/>
        </radialGradient>
        <linearGradient id="swoosh" x1="0" y1="0" x2="1" y2="1">
          <stop offset="0" stop-color="#8f6fe0" stop-opacity="0.55"/>
          <stop offset="1" stop-color="#6a35c4" stop-opacity="0.35"/>
        </linearGradient>
      </defs>
      <rect width="1154" height="603" fill="#4f1fa8"/>
      <path d="M0 420 C 120 200, 420 70, 760 60 C 950 55, 1090 30, 1154 0 L1154 603 L0 603 Z" fill="url(#swoosh)"/>
      <path d="M1154 470 C 1000 550, 820 590, 620 603 L1154 603 Z" fill="#6a35c4" opacity="0.6"/>
      <rect width="1154" height="603" fill="url(#flower-glow)"/>
    </svg>

    <div class="banner__product" role="img" aria-label="Product photo: silver chain necklace with two red heart-shaped garnet pendants"></div>

    <h2 class="slogan">
      <span class="slogan__line">Never fall</span>
      <span class="slogan__line slogan__line--indent">out of stone</span>
    </h2>

    <div class="brand">
      <span class="brand__name">Velanor</span>
      <span class="brand__tagline">FINE GEMSTONE JEWELRY</span>
    </div>

    <p class="pitch">
      <span class="pitch__line">A Party Queen doesn't need to worry</span>
      <span class="pitch__line">whenever she may meet an embarrassing</span>
      <span class="pitch__line">moment - a stone of jewelry falls out</span>
      <span class="pitch__line">at a very important occasion</span>
    </p>

    <p class="visit">visit: http://velanor-shop.example/</p>
  </section>
</body>
</html>
```